Rack Card for IV Infusion Vitamin Supplement bar

We need a very eye catching rack card so that customers would instantly know it is for IV vitamin infusions. We have our previous rack card (pdf) as an example that did not bring in any clients as an example as well as another one that we did not like too much. The bar is for people to feel better with hydration and vitamins.

Target Market(s)

Anyone

Industry/Entity Type

Healthcare

Requirements
Must have
• Logo on rack card
Should not have
• Not pink other than the logo

```html
<!DOCTYPE html>
<html lang="en">
<head>
<meta charset="utf-8">
<title>Solace Health &amp; Wellness – Rack Card</title>
<link href="https://fonts.googleapis.com/css2?family=Poppins:wght@400;500;600;700;800&family=Bebas+Neue&family=Montserrat:wght@500;600;800&display=swap" rel="stylesheet">
<style>
  :root{
    --brand:#e23f8b;
    --accent:#e8731a;
    --accent-soft:#f7b77a;
    --green:#1f5c47;
    --green-dark:#0f4a31;
    --ink:#222;
    --muted:#454545;
    --paper:#efefef;
    --paper-deep:#e2e2e2;
    --canvas:#ffffff;
  }
  *{box-sizing:border-box;margin:0;padding:0}
  html,body{width:1200px;height:2400px;overflow:hidden;background:var(--canvas)}
  body{position:relative;font-family:"Poppins",sans-serif;color:var(--ink)}
  .card{position:absolute;top:611px;width:541px;height:1178px;overflow:hidden;background:var(--paper);box-shadow:0 6px 18px rgba(0,0,0,.18)}
  .card--front{left:45px}
  .card--back{left:614px;background:#fff}
  .abs{position:absolute}

  /* front */
  .corner-disc{left:380px;top:-16px;width:180px;height:180px;border-radius:50%;background:#c8c8c8}
  .brand{left:0;width:100%;top:50px;text-align:center;color:var(--green)}
  .brand-dot{display:block;width:54px;height:54px;border-radius:50%;background:var(--brand);margin:0 auto 16px}
  .brand-name{font-family:"Poppins",sans-serif;font-weight:500;font-size:40px;letter-spacing:10px;line-height:1}
  .brand-tag{font-family:"Poppins",sans-serif;font-weight:500;font-size:12px;letter-spacing:5px;margin-top:6px}
  .headline{left:0;width:100%;top:205px;text-align:center;font-weight:800;line-height:.92}
  .headline .big{display:block;color:var(--accent);font-size:92px;letter-spacing:-1px}
  .headline .sub{display:block;color:var(--green);font-size:58px;letter-spacing:-.5px}
  .photo-fruit{left:0;top:405px;width:541px;height:400px;
    background:
      radial-gradient(circle at 60% 22%,#f5a640 0 70px,transparent 72px),
      radial-gradient(circle at 30% 20%,#c5d96a 0 40px,transparent 42px),
      radial-gradient(circle at 35% 50%,#6a9e3a 0 42px,transparent 44px),
      radial-gradient(circle at 48% 64%,#f29a3c 0 64px,transparent 66px),
      radial-gradient(circle at 80% 56%,#f47a5a 0 58px,transparent 60px),
      radial-gradient(circle at 96% 58%,#f8a52f 0 50px,transparent 52px),
      linear-gradient(180deg,#f0f0f0,#fafafa 40%,#f2f2f2)}
  .book-badge{width:190px;height:190px;border-radius:50%;background:var(--accent);border:9px solid var(--accent-soft);display:flex;flex-direction:column;align-items:center;justify-content:center;font-family:"Bebas Neue",sans-serif;line-height:.82;transform:rotate(-8deg)}
  .book-badge .l1{color:var(--green-dark);font-size:74px}
  .book-badge .l2{color:#fff;font-size:80px}
  .card--front .book-badge{left:290px;top:606px}
  .lower-disc{left:-180px;top:775px;width:850px;height:850px;border-radius:50%;background:var(--paper-deep)}
  .lower-white{left:0;top:775px;width:541px;height:420px;background:#fff}
  .question{left:0;width:100%;top:840px;text-align:center;font-weight:700;font-size:41px;line-height:1.08;color:var(--ink)}
  .contact-pill{left:62px;top:982px;width:410px;height:46px;border-radius:10px;background:var(--green-dark);color:#fff;font-family:"Montserrat",sans-serif;font-weight:800;font-size:29px;letter-spacing:6px;text-align:center;line-height:46px}
  .phone{left:0;width:100%;text-align:center;color:var(--accent);font-family:"Montserrat",sans-serif;font-weight:800;font-size:52px;line-height:1}
  .address{left:0;width:100%;text-align:center;font-family:"Montserrat",sans-serif;font-weight:500;font-size:20px}
  .web{left:0;width:100%;text-align:center;font-family:"Montserrat",sans-serif;font-weight:600;font-size:21px;letter-spacing:3px}
  .card--front .phone{top:1065px}
  .card--front .address{top:1116px}
  .card--front .web{top:1146px}

  /* back */
  .back-top{left:0;top:0}
  .section-title{left:35px;color:var(--green);font-weight:800;line-height:1}
  .title-premium{top:35px;font-size:37px}
  .title-addons{top:772px;font-size:28px}
  .service{display:flex;align-items:center;gap:6px}
  .service-icon{width:32px;height:32px;border-radius:50%;border:2px solid var(--green);background:#fff;flex:none;display:flex;align-items:center;justify-content:center}
  .service-icon::after{content:"";width:14px;height:14px;border-radius:50%;border:2px solid var(--green)}
  .service-name{color:var(--green);font-weight:700;font-size:16px;line-height:1.05;text-transform:uppercase}
  .service-desc{font-size:13px;line-height:1.18;color:var(--muted)}
  .col-left{left:35px}
  .col-right{left:287px}
  .desc-left{left:35px;width:225px}
  .desc-right{left:284px;width:240px}
  .photo-orange{left:260px;top:505px;width:290px;height:250px;border-radius:50% 0 0 50%;
    background:radial-gradient(circle at 65% 55%,#f7c23a 0 40%,#f29422 58%,#fbe3b0 64%,transparent 66%)}
  .card--back .book-badge{left:308px;top:553px}
  .addon{display:flex;gap:8px;align-items:flex-start;font-size:17px;line-height:1.2;color:var(--ink);text-transform:uppercase}
  .addon::before{content:"";width:11px;height:11px;border-radius:50%;background:var(--green);margin-top:4px;flex:none}
  .addon small{display:block;text-transform:none;font-size:12.5px;line-height:1.15;color:var(--muted)}
  .card--back .phone{top:1047px}
  .card--back .address,.card--back .web{color:#fff}
  .card--back .address{top:1098px}
  .card--back .web{top:1126px}
</style>
</head>
<body>

<section class="card card--front">
  <div class="abs corner-disc"></div>
  <div class="abs brand">
    <span class="brand-dot"></span>
    <div class="brand-name">SOLACE</div>
    <div class="brand-tag">HEALTH &amp; WELLNESS</div>
  </div>
  <h1 class="abs headline">
    <span class="big">VITAMIN</span>
    <span class="sub">INFUSIONS AND</span>
    <span class="sub">INJECTIONS</span>
  </h1>
  <div class="abs photo-fruit" role="img" aria-label="Photo of citrus fruits, limes, kiwi, leaves, vitamin ampoules and a syringe on white"></div>
  <div class="abs lower-white"></div>
  <div class="abs lower-disc"></div>
  <div class="abs book-badge"><span class="l1">BOOK</span><span class="l2">NOW</span></div>
  <p class="abs question">ARE YOU<br>READY FOR BETTER<br>HEALTH CARE?</p>
  <div class="abs contact-pill">CONTACT US NOW</div>
  <div class="abs phone">555-014-2290</div>
  <div class="abs address">1420 N. Oak St., STE 2B Riverton</div>
  <div class="abs web">www.solacetotalhealth.com</div>
</section>

<section class="card card--back">
  <svg class="abs back-top" width="541" height="1178" viewBox="0 0 541 1178" aria-hidden="true">
    <path d="M0,0 H541 V480 C530,650 450,752 300,752 C150,752 5,700 0,540 Z" fill="#ececec"/>
    <path d="M0,540 C5,700 150,752 300,752 C450,752 530,650 541,480" fill="none" stroke="#e8731a" stroke-width="5"/>
    <path d="M0,1178 V1065 Q0,1022 60,1022 H481 Q541,1022 541,1065 V1178 Z" fill="#0f4a31"/>
    <path d="M0,1065 Q0,1022 60,1022 H481 Q541,1022 541,1065" fill="none" stroke="#e8731a" stroke-width="6"/>
  </svg>
  <div class="abs photo-orange" role="img" aria-label="Photo of a halved orange slice"></div>

  <h2 class="abs section-title title-premium">PREMIUM INFUSIONS</h2>

  <div class="abs service col-left" style="top:88px"><span class="service-icon"></span><span class="service-name">Solace Cocktail</span></div>
  <p class="abs service-desc desc-left" style="top:124px">Reduce stress, fatigue, and boost your energy. Solace client favorite! (IV fluids, Vitamin C, B-complex, B12, and electrolytes)</p>

  <div class="abs service col-left" style="top:191px"><span class="service-icon"></span><span class="service-name">Immune Support</span></div>
  <p class="abs service-desc desc-left" style="top:227px">Protect the immune system when risk of illness is high. Great for pre, post-travel (IV fluids, Vitamin C, B-complex, and Zinc)</p>

  <div class="abs service col-left" style="top:300px"><span class="service-icon"></span><span class="service-name">Sports Recovery</span></div>
  <p class="abs service-desc desc-left" style="top:336px">Recover fast from illness, exhaustion, and workouts. (IV fluids, B-complex, B12, and amino acids, and electrolytes)</p>

  <div class="abs service col-left" style="top:406px"><span class="service-icon"></span><span class="service-name">Brain Power</span></div>
  <p class="abs service-desc desc-left" style="top:443px">Recover fast from illness, exhaustion, and workouts. (IV fluids, B-complex, B12, and amino acids, and electrolytes)</p>

  <div class="abs service col-left" style="top:514px"><span class="service-icon"></span><span class="service-name">NAD+ 125G/ 250G/<br>500G Drip</span></div>
  <p class="abs service-desc desc-left" style="top:556px">Enhance your cognitive health and help reverse aging. Promotes cell regeneration. Can aid mental clarity, better sleep, and energy</p>

  <div class="abs service col-right" style="top:94px"><span class="service-icon"></span><span class="service-name">The Glow</span></div>
  <p class="abs service-desc desc-right" style="top:130px">Give a glowing boost to skin and hair from inside out. (IV fluids, Glutathione, Vitamin B-complex, and Biotin)</p>

  <div class="abs service col-right" style="top:204px"><span class="service-icon"></span><span class="service-name">Energized</span></div>
  <p class="abs service-desc desc-right" style="top:242px">Boost metabolism, burn fat easier, and feel energized. (IV fluids, B-complex, and amino acid blend)</p>

  <div class="abs service col-right" style="top:311px"><span class="service-icon"></span><span class="service-name">The Jetlag Drip</span></div>
  <div class="abs service col-right" style="top:354px"><span class="service-icon"></span><span class="service-name">The Migraine / PMS Drip</span></div>
  <div class="abs service col-right" style="top:398px"><span class="service-icon"></span><span class="service-name">The Hangover Drip</span></div>
  <div class="abs service col-right" style="top:440px"><span class="service-icon"></span><span class="service-name">High Dose Vitamin C</span></div>

  <div class="abs book-badge"><span class="l1">BOOK</span><span class="l2">NOW</span></div>

  <h2 class="abs section-title title-addons">INFUSIONS ADD-ONS</h2>
  <div class="abs addon" style="left:35px;top:815px;width:240px"><span>Glutathione<small>By appointments only, including weekends</small></span></div>
  <div class="abs addon" style="left:35px;top:882px;width:240px"><span>Additional<br>Vitamin C</span></div>
  <div class="abs addon" style="left:35px;top:940px"><span>Additional Zinc</span></div>
  <div class="abs addon" style="left:35px;top:982px"><span>Additional Magnesium</span></div>
  <div class="abs addon" style="left:303px;top:815px;width:230px"><span>Anti- Inflammation Medication</span></div>
  <div class="abs addon" style="left:303px;top:880px;width:230px"><span>Anti-Nausea<br>Medication</span></div>
  <div class="abs addon" style="left:303px;top:938px"><span>Vitamin D Shot</span></div>
  <div class="abs addon" style="left:303px;top:980px"><span>Vitamin B12 Shot</span></div>

  <div class="abs phone">555-014-2290</div>
  <div class="abs address">1420 N. Oak St., STE 2B Riverton</div>
  <div class="abs web">www.solacetotalhealth.com</div>
</section>

</body>
</html>
```